Sponsorenmappe für die Lindenhof Jugend Bewegungs Institut
Zielgruppe
Die Lindenhof Jugend Bewegungs Institut (LJBI) bietet Schulen und Vereinen vielfältige Sport-, Bewegungs- und Ernährungsangebote.
Mit der Lindenhof Jugend Kick Institut (LJKI) und der Jugend Kick Institut (JKI) hat die LJBI-GmbH für den Fußballbereich zwei eigene Marken.
Das ganzheitliche LJBI-Konzept fördert ein sinnvolles Zusammenspiel von Schule, Sport und Persönlichkeitsentwicklung.
Das Design der Sponsorenmappe sollte natürlich in erster Linie den (vorallem mittelständischen) potentiellen Sponsoren gefallen und diese ansprechen. Hier sollte das Design klar und strukturiert sein, jedoch kleine Einflüsse der kinderaffinenen Marken besitzen.
Aufgabenstellung
Anbei haben wir schon einmal eine "Sponsorenmappe" in Word entworfen. Hierbei handelt es sich nur um einen kleinen Vorschlag wie es vielleicht aussehen könnte!
Die Textbausteine sollen jedoch verwendet werden.
Format: Din A4 - Druckdatenblatt von Papierwelle liegt bei.
Vorder- und Rückseite der Broschüre sind schon angefertig! Diese müssen noch noch angefügt werden. Tendenziell sollte die Broschüre dieses Design aufgreifen. Auch die erste Klappseite (Auf dem Druckdatenblatt als "E" gekennzeichnet - bei "D") ist schon designt. Hierbei handelt es sich um das Organigramm der LJBI (siehe Anhang). Überschrift muss jedoch noch in der jeweiligen Schriftart eingefügt werden.
Anbei finden Sie eine Win-Rar-Datei mit Logos und Bildern, die Ihnen zur Verwendung stehen.
Zudem unsere Broschüre für weitere Infos
Dem Rest geben wir küntlerische Freiheit.

```html
<!DOCTYPE html>
<html lang="de">
<head>
<meta charset="utf-8">
<title>Sponsorenmappe LJBI</title>
<link href="https://fonts.googleapis.com/css2?family=Encode+Sans+Condensed:wght@400;500;600;700&display=swap" rel="stylesheet">
<style>
  :root{
    --blue:#009fe3;
    --white:#ffffff;
    --grey:#efefef;
    --ink:#1d1d1b;
    --photo-water:#4fb3e0;
    --photo-grass:#8cb548;
    --photo-beach:#8d9fb3;
    --photo-room:#e9e2d2;
    --photo-building:#6f8d5a;
  }
  *{margin:0;padding:0;box-sizing:border-box}
  html,body{width:1200px;height:663px;overflow:hidden;background:var(--white)}
  body{font-family:"Encode Sans Condensed",sans-serif;color:var(--ink)}
  .sheet{position:relative;width:1200px;height:663px;overflow:hidden}
  .abs{position:absolute}

  .flap-panel{left:0;top:0;width:396px;height:551px;background:var(--blue);border-right:1px solid var(--white);border-bottom:1px solid var(--white)}
  .top-strip{left:400px;top:0;width:800px;height:119px;background:linear-gradient(#ffffff,#f4f4f4)}
  .blue-band{left:400px;top:119px;width:800px;height:239px;background:var(--blue)}
  .grey-field{left:400px;top:358px;width:800px;height:193px;background:linear-gradient(#f2f2f2,#ebebeb)}
  .bottom-band{left:0;top:551px;width:1200px;height:112px;background:var(--blue)}
  .cut-lines{left:0;top:0;width:1200px;height:663px;pointer-events:none}

  .org-title{left:33px;top:42px;font-size:16px;color:var(--white);font-weight:400}
  .org-box{background:var(--white);display:flex;align-items:center;justify-content:center;text-align:center;font-size:10.5px;line-height:1.15;color:var(--ink)}
  .brand{display:flex;align-items:center;gap:4px;text-align:left}
  .brand-dot{width:20px;height:20px;border-radius:50%;border:2px solid var(--blue);flex:none}
  .brand-name{font-size:5.6px;font-weight:700;line-height:1.05;text-transform:uppercase;color:var(--ink)}
  .brand-lg .brand-dot{width:34px;height:34px;border-width:3px}
  .brand-lg .brand-name{font-size:9.2px}
  .brand-sm .brand-dot{width:14px;height:14px;border-width:1.5px}
  .brand-sm .brand-name{font-size:4.6px}

  .photo{background:var(--photo-water)}
  .contact{left:433px;top:230px;font-size:5.6px;line-height:9.2px;color:var(--white)}
  .contact p+p{margin-top:9px}
  .marks-title{left:434px;top:455px;font-size:5.6px;font-weight:700}
  .mark-url{font-size:5px;top:501px}
  .sponsoring{right:37px;top:457px;font-size:17px;font-weight:400}
</style>
</head>
<body>
<div class="sheet">
  <div class="abs flap-panel"></div>
  <div class="abs top-strip"></div>
  <div class="abs blue-band"></div>
  <div class="abs grey-field"></div>
  <div class="abs bottom-band"></div>

  <svg class="abs cut-lines" viewBox="0 0 1200 663">
    <g fill="none" stroke="#ffffff" stroke-width="0.7" stroke-dasharray="2 2">
      <line x1="395" y1="0" x2="395" y2="551"/>
      <line x1="400" y1="0" x2="400" y2="551"/>
      <line x1="796" y1="119" x2="796" y2="358"/>
      <line x1="799" y1="119" x2="799" y2="358"/>
      <line x1="400" y1="557" x2="796" y2="557"/>
    </g>
    <g fill="none" stroke="#ffffff" stroke-width="0.8">
      <line x1="400" y1="551" x2="796" y2="551"/>
      <polyline points="400,551 400,621 443,663"/>
      <polyline points="796,551 796,621 757,663"/>
    </g>
    <!-- organigram connectors -->
    <g fill="none" stroke="#ffffff" stroke-width="1.2">
      <line x1="197" y1="155" x2="197" y2="247"/>
      <polyline points="68,179 68,166 325,166 325,179"/>
      <line x1="154" y1="166" x2="154" y2="179"/>
      <line x1="240" y1="166" x2="240" y2="179"/>
      <line x1="197" y1="283" x2="197" y2="395"/>
      <polyline points="95,307 95,294 299,294 299,307"/>
      <polyline points="95,395 95,382 299,382 299,395"/>
    </g>
  </svg>

  <h1 class="abs org-title">Organigramm</h1>

  <div class="abs org-box" style="left:131px;top:119px;width:131px;height:36px">
    <div class="brand"><span class="brand-dot"></span><span class="brand-name">Lindenhof Jugend<br>Bewegungs Institut GmbH</span></div>
  </div>
  <div class="abs org-box" style="left:32px;top:179px;width:73px;height:36px">Schulkoopera-<br>tionen</div>
  <div class="abs org-box" style="left:118px;top:179px;width:73px;height:36px">LJBI e.V.</div>
  <div class="abs org-box" style="left:203px;top:179px;width:73px;height:36px">Shop</div>
  <div class="abs org-box" style="left:289px;top:179px;width:73px;height:36px">Marketing</div>

  <div class="abs org-box" style="left:131px;top:247px;width:131px;height:36px">
    <div class="brand"><span class="brand-dot"></span><span class="brand-name">Lindenhof Jugend<br>Bewegungs Institut GmbH</span></div>
  </div>
  <div class="abs org-box" style="left:50px;top:307px;width:87px;height:36px">Spezialtraining</div>
  <div class="abs org-box" style="left:256px;top:307px;width:87px;height:36px">Schulungen</div>
  <div class="abs org-box" style="left:154px;top:337px;width:86px;height:37px">
    <div class="brand"><span class="brand-dot" style="width:14px;height:14px"></span><span class="brand-name">Jugend Kick<br>Institut</span></div>
  </div>
  <div class="abs org-box" style="left:50px;top:395px;width:87px;height:36px">Camps</div>
  <div class="abs org-box" style="left:154px;top:395px;width:86px;height:36px">Reisen</div>
  <div class="abs org-box" style="left:256px;top:395px;width:87px;height:36px">Individualtraining</div>

  <div class="abs brand brand-lg" style="left:1002px;top:46px">
    <span class="brand-dot"></span><span class="brand-name">Lindenhof Jugend<br>Bewegungs Institut GmbH</span>
  </div>

  <div class="abs photo" role="img" aria-label="Foto des Vereinsgebäudes mit Rasenfläche und Bäumen" style="left:433px;top:154px;width:123px;height:50px;background:linear-gradient(#c9d9e6 0%,#9fb0a4 45%,var(--photo-building) 100%)"></div>

  <div class="abs contact">
    <p>KONTAKT<br>Lindenhof Jugend Bewegungs Institut GmbH<br>Geschäftsstelle<br>Lindenweg 12<br>D-70999 Musterstadt<br>T +49 (0)7000 1234560</p>
    <p>info@ljbi-beispiel.de<br>www.ljbi-beispiel.de</p>
  </div>

  <div class="abs photo" role="img" aria-label="Foto: Kind beim Schwimmen im Becken" style="left:833px;top:133px;width:103px;height:73px;background:linear-gradient(160deg,#2f8fd0,var(--photo-water),#a8d8ef)"></div>
  <div class="abs photo" role="img" aria-label="Illustration: Weltkugel mit bunten Figuren" style="left:946px;top:133px;width:103px;height:73px;background:radial-gradient(circle,#3a6fb5 0 22%,#ffffff 40%)"></div>
  <div class="abs photo" role="img" aria-label="Foto: Kinder beim Spielen in der Turnhalle" style="left:1058px;top:133px;width:103px;height:73px;background:linear-gradient(135deg,#f3efe4,var(--photo-room),#c9d4de)"></div>
  <div class="abs photo" role="img" aria-label="Foto: drei Kinder mit Bällen auf der Wiese" style="left:833px;top:216px;width:159px;height:128px;background:linear-gradient(160deg,#a6c95a,var(--photo-grass),#d9a08a)"></div>
  <div class="abs photo" role="img" aria-label="Foto: Trainer mit Kindergruppe am Strand" style="left:1002px;top:216px;width:160px;height:128px;background:linear-gradient(#6f9ab9,var(--photo-beach) 45%,#d8c9ad)"></div>

  <div class="abs marks-title">Marken der LJBI-GmbH</div>
  <div class="abs brand brand-sm" style="left:432px;top:480px">
    <span class="brand-dot"></span><span class="brand-name">Lindenhof Jugend<br>Kick Institut</span>
  </div>
  <div class="abs mark-url" style="left:433px">www.ljki-beispiel.de</div>
  <div class="abs brand brand-sm" style="left:568px;top:480px">
    <span class="brand-dot"></span><span class="brand-name">Jugend Kick<br>Institut</span>
  </div>
  <div class="abs mark-url" style="left:567px">www.jki-beispiel.de</div>

  <div class="abs sponsoring">Sponsoring</div>
</div>
</body>
</html>
```